Innovation Presentation Template

I need a unique template design for a presentation on Innovation used exclusively inside of our company. I'd prefer to work in Apple Keynote but can take a .ppt and convert it. The template should appeal to a broad audience of diverse job descriptions. This is a one-time presentation that will last between 30 and 45 minutes. The design should provide a strong visual appeal with multiple chart layouts to support highlighted test points (no bullets, I hate bullets), graphics, line art, and video/photos. My presentations are sparse, never more that 2 concepts per chart (usually one). Our company is a high tech manufacturer selling products in many markets ranging from Government to consumer. The final design should include style a style guide including suggested fonts, colors, graph formats, suggested word art, etc.

Target Market(s)

The audience is internal employees only. Strong corporate branding is not required in this presentation.

Industry/Entity Type

Government

Colors
3277b5
faa54b

Requirements
Must have
• Strong visual appeal helping to support the communication of simple concepts (that have been broken down from complex subject matter).

Multiple chart template forms to support different forms of communication including text points, data charts, graphics, photos, and videos.

Visuals will be memorable, but not overpower the content. Visuals will help convey the content.

Well conceived and coordinated color pallets. Fonts guides (that I can access).

You can visit our company web site at www.KOVEX.com to see logo and corporate look/feel. It would be good to build logo into a few of the chart templates, but not all.
Nice to have
• Keynote (please). I can live with .ppt if I have to.

Many charts will make a point with simple single sentences. Find a way to make the sentences graphically interesting by varying font and/or color of specific words to help drive points.

Note that colors that I've identified below are based upon the blue used in our logo and the orange that complements it. I'm not married to these but use them as guidelines.
Should not have
• Noise. Corporate nauseia.

```html
<!DOCTYPE html>
<html lang="en">
<head>
<meta charset="utf-8">
<title>Innovation Presentation Template – Slide Overview</title>
<link rel="stylesheet" href="https://fonts.googleapis.com/css2?family=Source+Sans+3:ital,wght@0,300;0,400;0,600;0,700;1,400&display=swap">
<style>
  :root{
    --orange:#ffa300;
    --black:#121212;
    --dark:#2b2b2b;
    --grey:#8a8a8a;
    --mid:#5a5a5a;
    --board:#c3c3c3;
    --navy:#1f3a8c;
    --paper-top:#ffffff;
    --paper-bottom:#ebebeb;
    --text:#707070;
  }
  *{box-sizing:border-box;margin:0;padding:0}
  html,body{width:1200px;height:900px;overflow:hidden}
  body{background:var(--board);font-family:"Source Sans 3",Arial,sans-serif;color:var(--text);position:relative}

  .slide{position:absolute;width:338px;height:262px;overflow:hidden;background:linear-gradient(var(--paper-top),var(--paper-bottom))}
  .abs{position:absolute}

  .slide-title{position:absolute;left:14px;top:16px;right:14px;font-size:13px;font-weight:300;color:#222;letter-spacing:.2px;border-bottom:.7px solid #b5b5b5;line-height:14px}
  .slide-title em{font-style:normal;color:var(--orange)}

  .footer{position:absolute;left:0;right:0;bottom:0;height:6px;background:#3b3b3b}
  .footer::after{content:"";position:absolute;right:0;top:0;width:92px;height:100%;background:var(--orange);clip-path:polygon(6px 0,100% 0,100% 100%,0 100%)}
  .footer .page{position:absolute;right:6px;top:-1px;font-size:5px;color:#fff;z-index:1}

  .brand{position:absolute;display:flex;align-items:center;gap:3px;font-weight:700;color:var(--navy);letter-spacing:.3px}
  .brand .mark{display:block;background:currentColor}
  .brand.small{left:8px;bottom:12px;font-size:11px}
  .brand.small .mark{width:7px;height:7px}
  .brand.light{color:#fff}

  .photo{position:absolute}
  .body{font-size:5.3px;line-height:9.6px;text-align:justify;color:var(--text)}
  .label{font-size:7px;color:var(--orange);letter-spacing:.2px}

  /* welcome */
  .welcome-title{left:28px;top:86px;font-size:15px;font-weight:300;color:#fff;line-height:18px}
  .welcome-title span{display:block;color:var(--orange)}
  .welcome-date{left:28px;top:126px;font-size:8.5px;color:#fff}
  .brand.large{font-size:23px}
  .brand.large .mark{width:14px;height:14px}

  /* team */
  .team-intro{left:40px;right:40px;top:50px;text-align:center;font-size:5.3px;line-height:7.5px;font-style:italic;color:var(--orange)}
  .member{position:absolute;top:80px;width:80px;text-align:center}
  .member .avatar{width:50px;height:50px;margin:0 auto;border-radius:50%;border:2px solid var(--orange);background:radial-gradient(circle at 50% 40%,#e6e6e6,#9a9a9a)}
  .member .name{margin-top:10px;font-size:5.5px;color:#222}
  .member .role{font-size:4.2px;font-style:italic;color:#666}
  .member .bio{margin:8px 4px 0;font-size:4.3px;line-height:9.2px;text-align:justify;color:#9a9a9a}

  /* chart */
  .stat{position:absolute;top:66px;width:94px;text-align:center}
  .stat .pct{margin-top:8px;font-size:9px;color:var(--orange)}
  .stat .caption{margin-top:5px;font-size:4.3px;line-height:5.4px;color:#888}

  /* mission */
  .quote{left:40px;top:90px;width:104px;text-align:center}
  .quote .mark-q{font-size:16px;color:#b0b0b0;font-style:italic;line-height:10px;font-weight:700}
  .quote .who{font-size:7px;color:var(--orange);margin:3px 0 4px}
  .quote p{font-size:5.5px;line-height:12px;font-style:italic;font-weight:600;color:#555}

  /* people */
  .band-dark{left:0;right:0;top:166px;bottom:0;background:var(--dark)}
  .pillar{position:absolute;top:156px;width:100px;text-align:center}
  .pillar .icon{width:24px;height:24px;margin:0 auto;border-radius:50%;background:var(--orange);display:flex;align-items:center;justify-content:center}
  .pillar h3{margin-top:5px;font-size:7.2px;font-weight:700;color:var(--orange)}
  .pillar p{margin-top:2px;font-size:4.2px;line-height:5.4px;color:#a9a9a9}

  /* thank you */
  .thanks{left:101px;top:113px;font-size:14px;font-weight:300;color:var(--orange);line-height:15px}
  .thanks small{display:block;font-size:6.5px;color:#ddd}
  .contacts{left:198px;top:90px;list-style:none}
  .contacts li{display:flex;align-items:center;gap:5px;font-size:7.5px;color:#fff;height:13.5px}
  .contacts li i{width:8px;height:8px;border-radius:50%;background:var(--orange);display:block}
  .social{left:197px;top:147px;display:flex;gap:4px}
  .social span{width:12px;height:12px;background:var(--orange);display:block}
</style>
</head>
<body>

<!-- 1 Welcome -->
<section class="slide" style="left:74px;top:40px">
  <svg class="abs" width="338" height="262" viewBox="0 0 338 262" aria-hidden="true">
    <polygon points="0,55 104,55 114,65 0,65" fill="var(--orange)"/>
    <polygon points="0,65 218,65 228,55 338,55 338,175 0,175" fill="var(--black)"/>
    <polygon points="122,175 154,175 170,190 138,190" fill="var(--orange)"/>
    <polygon points="154,175 338,175 338,190 170,190" fill="#6b6b6b"/>
  </svg>
  <div class="photo" role="img" aria-label="Product photo: handheld device with thermal camera attachment" style="left:252px;top:74px;width:70px;height:101px;border-radius:10px 10px 0 0;background:linear-gradient(90deg,#2a2a2a,#6a6a6a 50%,#333)"></div>
  <h1 class="abs welcome-title" style="font-weight:300">WELCOME<span>TO OUR PRESENTATION</span></h1>
  <p class="abs welcome-date">Birmingham, August 25, 2014</p>
  <div class="brand large" style="left:36px;top:210px"><span class="mark"></span>KOVEX</div>
</section>

<!-- 2 Products -->
<section class="slide" style="left:425px;top:40px">
  <h2 class="slide-title">OUR <em>PRODUCTS</em></h2>
  <div class="abs" style="left:0;right:0;top:74px;height:69px;background:var(--orange)"></div>
  <p class="abs body" style="left:41px;width:166px;top:94px;color:#fff;line-height:12px">consectetur adipiscing elit, sed do eiusmod tempor incididunt ut labore et dolore magna aliqua. Ut enim ad minim veniam, quis nostrud exercitation ullamco laboris</p>
  <p class="abs body" style="left:41px;width:166px;top:148px;line-height:12px">Lorem ipsum dolor sit amet, consectetur adipiscing elit, sed do eiusmod tempor incididunt ut labore et dolore magna aliqua. Ut enim ad minim veniam, quis nostrud exercitation ullamco laboris nisi ut aliquip ex ea commodo consequat. Duis aute irure dolor in reprehenderit in voluptate velit esse cillum dolore eu fugiat nulla pariatur.</p>
  <div class="photo" role="img" aria-label="Product photo: phone in thermal camera case showing a thermal image" style="left:243px;top:42px;width:62px;height:152px;border-radius:8px;background:linear-gradient(#2b2b2b 0 8%,#7b2da0 8%,#e0601a 50%,#ffb000 80%,#222 80%)"></div>
  <div class="brand small"><span class="mark"></span>KOVEX</div>
  <div class="footer"><span class="page">2</span></div>
</section>

<!-- 3 Products detail -->
<section class="slide" style="left:775px;top:40px">
  <h2 class="slide-title">OUR <em>PRODUCTS</em></h2>
  <div class="photo" role="img" aria-label="Close-up product photo of the camera lens module" style="left:15px;top:38px;width:311px;height:76px;background:radial-gradient(ellipse at 45% 50%,#8a8a8a,#222 60%,#111)"></div>
  <h3 class="abs label" style="left:22px;top:132px;font-weight:400">OUR HISTORY</h3>
  <p class="abs body" style="left:22px;top:144px;width:145px;line-height:12px">Lorem ipsum dolor sit amet, consectetur adipiscing elit, sed do eiusmod tempor incididunt ut labore et dolore magna aliqua. Ut enim ad minim veniam, quis nostrud exercitation ullamco laboris nisi ut aliquip ex ea commodo consequat. Duis aute irure dolor in reprehenderit in voluptate velit esse cillum</p>
  <h3 class="abs label" style="left:178px;top:132px;font-weight:400">OUR ACHIEVEMENT</h3>
  <p class="abs body" style="left:178px;top:144px;width:145px;line-height:12px">Lorem ipsum dolor sit amet, consectetur adipiscing elit, sed do eiusmod tempor incididunt ut labore et dolore magna aliqua. Ut enim ad minim veniam, quis nostrud exercitation ullamco laboris nisi ut aliquip ex ea commodo consequat. Duis aute irure dolor in reprehenderit in voluptate velit esse cillum</p>
  <div class="brand small"><span class="mark"></span>KOVEX</div>
  <div class="footer"><span class="page">2</span></div>
</section>

<!-- 4 Image & texts -->
<section class="slide" style="left:74px;top:316px;background:var(--black)">
  <div class="abs" style="left:0;top:0;width:171px;height:262px;background:var(--orange)"></div>
  <h2 class="abs" style="left:26px;top:46px;font-size:13px;font-weight:300;color:#fff">IMAGE <span style="color:#fff">&amp;</span> <span style="color:var(--black)">TEXTS</span></h2>
  <div class="abs" style="left:167px;top:50px;width:8px;height:8px;background:#fff"></div>
  <h3 class="abs" style="left:20px;top:126px;font-size:7px;font-weight:400;color:#fff">OUR ACHIEVEMENT</h3>
  <p class="abs body" style="left:20px;top:137px;width:142px;color:#fff;line-height:12px">Lorem ipsum dolor sit amet, consectetur adipiscing elit, sed do eiusmod tempor incididunt ut labore et dolore magna aliqua. Ut enim ad minim veniam, quis nostrud exercitation ullamco laboris nisi ut aliquip ex ea commodo consequat. Duis aute irure dolor in reprehenderit in voluptate velit esse cillum</p>
  <div class="photo" role="img" aria-label="Product photo: phone in thermal case displaying a thermal image of a wall" style="left:218px;top:48px;width:78px;height:178px;border-radius:9px;background:linear-gradient(#333 0 10%,#5b1f8f 10%,#c43b6b 40%,#ffb300 60%,#7a2aa0 82%,#333 82%)"></div>
  <div class="brand small light"><span class="mark"></span>KOVEX</div>
</section>

<!-- 5 Team -->
<section class="slide" style="left:425px;top:316px">
  <h2 class="slide-title">OUR <em>TEAM</em></h2>
  <p class="abs team-intro">Our team of expert consultants brings a total of 100 years of experience<br>in the industry, 50 years in consultingation across the country to your facility to address needs</p>
  <div class="member" style="left:43px">
    <div class="avatar" role="img" aria-label="Portrait photo of team member"></div>
    <div class="name">JONATHAN DOE</div><div class="role">President</div>
    <p class="bio">dolor sit amet, consectetur adipiscing elit, sed do eiusmod tempor incididunt ut labore et dolore magna aliqua. Ut enim ad minim veniam, quis nostrud exercitation</p>
  </div>
  <div class="member" style="left:126px">
    <div class="avatar" role="img" aria-label="Portrait photo of team member"></div>
    <div class="name">MELANIE DOE</div><div class="role">CEO / Founder</div>
    <p class="bio">dolor sit amet, consectetur adipiscing elit, sed do eiusmod tempor incididunt ut labore et dolore magna aliqua. Ut enim ad minim veniam, quis nostrud exercitation</p>
  </div>
  <div class="member" style="left:210px">
    <div class="avatar" role="img" aria-label="Portrait photo of team member"></div>
    <div class="name">NATALIE DOE</div><div class="role">Vice President</div>
    <p class="bio">dolor sit amet, consectetur adipiscing elit, sed do eiusmod tempor incididunt ut labore et dolore magna aliqua. Ut enim ad minim veniam, quis nostrud exercitation</p>
  </div>
  <div class="brand small"><span class="mark"></span>KOVEX</div>
  <div class="footer"><span class="page">2</span></div>
</section>

<!-- 6 Chart -->
<section class="slide" style="left:775px;top:316px">
  <h2 class="slide-title">OUR <em>CHART</em></h2>
  <div class="stat" style="left:27px">
    <svg width="68" height="68" viewBox="0 0 68 68" aria-hidden="true">
      <circle cx="34" cy="34" r="28" fill="none" stroke="#6e6e6e" stroke-width="7"/>
      <circle cx="34" cy="34" r="28" fill="none" stroke="var(--orange)" stroke-width="7" stroke-dasharray="142.5 175.9" transform="rotate(-90 34 34)"/>
      <circle cx="34" cy="23" r="3.2" fill="var(--navy)"/>
      <rect x="30.5" y="27.5" width="7" height="16" rx="1.5" fill="var(--navy)"/>
    </svg>
    <div class="pct">81%</div>
    <p class="caption">dolor sit amet, consectetur adipiscing elit, sed do eiusmod tempor incididunt ut labore et dolore magna aliqua. Ut enim ad minim veniam, quis nostrud exercitation ullamco laboris nisi ut aliquip ex ea cillum dolore eu fugiat nulla pariatur.</p>
  </div>
  <div class="stat" style="left:123px">
    <svg width="68" height="68" viewBox="0 0 68 68" aria-hidden="true">
      <circle cx="34" cy="34" r="28" fill="none" stroke="var(--orange)" stroke-width="7"/>
      <circle cx="34" cy="34" r="28" fill="none" stroke="#2e2e2e" stroke-width="7" stroke-dasharray="126.6 175.9" transform="rotate(90 34 34)"/>
      <path d="M22 25h4l4 12h12l3-9H28" fill="none" stroke="var(--navy)" stroke-width="2.4" stroke-linejoin="round"/>
      <circle cx="31" cy="41" r="2" fill="var(--navy)"/><circle cx="41" cy="41" r="2" fill="var(--navy)"/>
    </svg>
    <div class="pct">72%</div>
    <p class="caption">dolor sit amet, consectetur adipiscing elit, sed do eiusmod tempor incididunt ut labore et dolore magna aliqua. Ut enim ad minim veniam, quis nostrud exercitation ullamco laboris nisi ut aliquip ex ea cillum dolore eu fugiat nulla pariatur.</p>
  </div>
  <div class="stat" style="left:227px">
    <svg width="68" height="68" viewBox="0 0 68 68" aria-hidden="true">
      <circle cx="34" cy="34" r="28" fill="none" stroke="#9a9a9a" stroke-width="7"/>
      <circle cx="34" cy="34" r="28" fill="none" stroke="var(--orange)" stroke-width="7" stroke-dasharray="40 175.9" transform="rotate(-90 34 34)"/>
      <rect x="24" y="25" width="20" height="13" fill="none" stroke="var(--navy)" stroke-width="2.4"/>
      <rect x="31" y="40" width="6" height="3" fill="var(--navy)"/>
    </svg>
    <div class="pct">63%</div>
    <p class="caption">dolor sit amet, consectetur adipiscing elit, sed do eiusmod tempor incididunt ut labore et dolore magna aliqua. Ut enim ad minim veniam, quis nostrud exercitation ullamco laboris nisi ut aliquip ex ea cillum dolore eu fugiat nulla pariatur.</p>
  </div>
  <div class="brand small"><span class="mark"></span>KOVEX</div>
  <div class="footer"><span class="page">2</span></div>
</section>

<!-- 7 Mission -->
<section class="slide" style="left:74px;top:590px">
  <h2 class="slide-title">OUR <em>MISSION</em></h2>
  <div class="abs quote">
    <div class="mark-q">"</div>
    <div class="who">WHO WE ARE</div>
    <p>dolor sit amet, consectetur adipiscing elit, sed do eiusmod tempor incididunt ut labore et dolore magna aliqua. Ut enim ad minim veniam, quis nostrud exercitation ullamco laboris nisi ut aliquip ex ea cesse cillum dolore eu fugiat nulla pariatur.</p>
    <div class="mark-q" style="margin-top:6px">"</div>
  </div>
  <h3 class="abs label" style="left:151px;top:100px;font-weight:400">OUR VALUES DEFINE WHO WE ARE</h3>
  <p class="abs body" style="left:151px;top:113px;width:166px;line-height:12px">Lorem ipsum dolor sit amet, consectetur adipiscing elit, sed do eiusmod tempor incididunt ut labore et dolore magna aliqua. Ut enim ad minim veniam, quis nostrud exercitation ullamco laboris nisi ut aliquip ex ea commodo consequat. Duis aute irure dolor in reprehenderit in voluptate velit esse cillum dolore eu fugiat nulla pariatur.</p>
  <div class="brand small"><span class="mark"></span>KOVEX</div>
  <div class="footer"><span class="page">2</span></div>
</section>

<!-- 8 People -->
<section class="slide" style="left:426px;top:590px">
  <div class="photo" role="img" aria-label="Black and white photo of a business team working together at a laptop" style="left:0;top:0;width:338px;height:166px;background:linear-gradient(90deg,#f4f4f4,#bdbdbd 45%,#7a7a7a 70%,#d9d9d9)"></div>
  <div class="abs band-dark"></div>
  <div class="pillar" style="left:10px">
    <div class="icon"><svg width="14" height="12" viewBox="0 0 14 12" aria-hidden="true"><circle cx="4" cy="3" r="2.2" fill="#222"/><circle cx="10" cy="3" r="2.2" fill="#222"/><path d="M0 11c0-3 2-4.5 4-4.5s4 1.5 4 4.5zM6 11c0-3 2-4.5 4-4.5s4 1.5 4 4.5z" fill="#222"/></svg></div>
    <h3>OUR PEOPLE</h3>
    <p>dolor sit amet, consectetur adipiscing elit, sed do eiusmod tempor incididunt ut labore et dolore magna aliqua. Ut enim ad minim veniam, quis nostrud exercitation ullamco laboris nisi ut aliquip ex ea cillum dolore eu fugiat nulla pariatur.</p>
  </div>
  <div class="pillar" style="left:118px">
    <div class="icon"><svg width="14" height="14" viewBox="0 0 14 14" aria-hidden="true"><g fill="none" stroke="#222" stroke-width="1.3"><circle cx="7" cy="7" r="6"/><ellipse cx="7" cy="7" rx="2.6" ry="6"/><path d="M1 7h12M2 4h10M2 10h10"/></g></svg></div>
    <h3>OUR GLOBALNESS</h3>
    <p>dolor sit amet, consectetur adipiscing elit, sed do eiusmod tempor incididunt ut labore et dolore magna aliqua. Ut enim ad minim veniam, quis nostrud exercitation ullamco laboris nisi ut aliquip ex ea cillum dolore eu fugiat nulla pariatur.</p>
  </div>
  <div class="pillar" style="left:231px">
    <div class="icon"><svg width="13" height="13" viewBox="0 0 13 13" aria-hidden="true"><rect x="1" y="4" width="6" height="6" fill="#222"/><rect x="6" y="1" width="6" height="6" fill="#222"/><circle cx="7" cy="10" r="2" fill="#222"/></svg></div>
    <h3>OUR PHILOSOPHY</h3>
    <p>dolor sit amet, consectetur adipiscing elit, sed do eiusmod tempor incididunt ut labore et dolore magna aliqua. Ut enim ad minim veniam, quis nostrud exercitation ullamco laboris nisi ut aliquip ex ea cillum dolore eu fugiat nulla pariatur.</p>
  </div>
  <div class="footer"><span class="page">2</span></div>
</section>

<!-- 9 Thank you -->
<section class="slide" style="left:778px;top:590px">
  <svg class="abs" width="338" height="262" viewBox="0 0 338 262" aria-hidden="true">
    <polygon points="0,54 58,54 68,67 0,67" fill="var(--orange)"/>
    <polygon points="0,67 338,67 338,162 0,162" fill="var(--black)"/>
    <polygon points="118,162 150,162 166,184 134,184" fill="var(--orange)"/>
    <polygon points="150,162 338,162 338,184 166,184" fill="#6b6b6b"/>
    <polygon points="100,162 118,162 134,184 116,184" fill="#8a8a8a"/>
  </svg>
  <div class="photo" role="img" aria-label="Orange line drawing of the thermal camera device" style="left:34px;top:75px;width:60px;height:87px;background:linear-gradient(90deg,#1a1a1a,#3a2a10 50%,#1a1a1a)"></div>
  <h2 class="abs thanks" style="font-weight:300">THANK YOU<small>For your time</small></h2>
  <ul class="abs contacts">
    <li><i></i>info@kovex.com</li>
    <li><i></i>www.KOVEX.com</li>
    <li><i></i>KOVEX</li>
    <li><i></i>+49 40 5550 1234</li>
  </ul>
  <div class="abs social" aria-label="Social links"><span></span><span></span><span></span></div>
  <div class="brand large" style="left:222px;top:218px"><span class="mark"></span>KOVEX</div>
</section>

</body>
</html>
```